Keelstone Advisory - Careerloom Header

I am a solopreneur with a consulting company. I do management consulting for small and mid-size manufacturers. There are two ways my prospects check me out - my web page, which went live this week (www.keelstoneadvisory.example), and my personal Careerloom page. I'm working on my Careerloom page now, and I'd like to have a header image that is unique and aligned with my brand.

My clients are smaller manufacturers, typically with 50-400 people. They are privately held, often by an individual or family, but sometimes by a professional investment group. They aren't as sophisticated as the Corvane 300 guys, and sometimes they struggle to grow because their processes break, or they don't have the right people or something else like that. I help them get through those issues.

Many of the people visiting the site will have a technical/engineering orientation, and most are in their late 40's to early 60's.

From my research, I think the image for my personal page is 1584x396, and this will be my primary page. The business page has a banner image size of 1536x768. I'd like to be able to use the same image in both.

Target Market(s)

Small and Mid-size manufacturers - C-Suite executives

Industry/Entity Type

Manufacturing

Font styles to use
Sans Serif

Colors

Designer to choose colors to be used in the design.

Requirements
Must have
• Logo incorporated. Be adaptable to both my personal Careerloom page and Business page, which have slightly different sizes.

```html
<!DOCTYPE html>
<html lang="en">
<head>
<meta charset="utf-8">
<title>Keelstone Advisory – Careerloom Header</title>
<link rel="stylesheet" href="https://fonts.googleapis.com/css2?family=Open+Sans:wght@400;600;700&display=swap">
<style>
  :root {
    --backdrop: #dfe7ed;
    --paper: #ffffff;
    --navy: #1f2766;
    --amber: #dc9431;
    --ink: #2b2b2b;
    --rule: #c8c8c8;
  }
  * { margin: 0; padding: 0; box-sizing: border-box; }
  html, body {
    width: 1095px;
    height: 1200px;
    overflow: hidden;
    background: var(--backdrop);
    font-family: "Open Sans", Arial, sans-serif;
  }
  .canvas { position: relative; width: 1095px; height: 1200px; }
  .size-label {
    position: absolute;
    font-size: 29px;
    color: var(--ink);
    transform: translateX(-50%);
    white-space: nowrap;
  }
  .size-label--profile { left: 564px; top: 118px; }
  .size-label--business { left: 517px; top: 587px; }
  .banner { position: absolute; display: block; background: var(--paper); }
  .banner--profile { left: 53px; top: 185px; width: 990px; height: 247px; }
  .banner--business { left: 148px; top: 644px; width: 798px; height: 399px; }
  .stripe-navy { fill: var(--navy); }
  .stripe-amber { fill: var(--amber); }
  .brand-mark { fill: var(--navy); }
  .brand-name { fill: var(--navy); font-weight: 600; }
  .brand-rule { stroke: var(--rule); stroke-width: 2; }
  .headline { font-weight: 700; fill: var(--ink); }
  .headline .accent { fill: var(--navy); }
  .body-copy { fill: var(--ink); }
</style>
</head>
<body>
<main class="canvas">
  <p class="size-label size-label--profile">1584 x 396</p>
  <svg class="banner banner--profile" viewBox="0 0 1238 309" aria-label="Careerloom profile header">
    <polygon class="stripe-navy" points="260,0 364,0 490,309 418,309"/>
    <polygon class="stripe-amber" points="398,129 486,129 554,260 1238,260 1238,309 490,309"/>

    <circle class="brand-mark" cx="55" cy="154" r="32"/>
    <line class="brand-rule" x1="110" y1="117" x2="110" y2="194"/>
    <text class="brand-name" x="124" y="158" font-size="34">Keelstone</text>
    <text class="brand-name" x="124" y="184" font-size="21" letter-spacing="2">Advisory</text>

    <text class="headline" x="564" y="106" font-size="33">BUSINESS <tspan class="accent">PAGE</tspan></text>
    <text class="body-copy" x="564" y="130" font-size="16.5">Lorem ipsum lorem ipsum, lorem</text>
    <text class="body-copy" x="564" y="151" font-size="16.5">ipsum lorem ipsum lorem ipsum</text>
    <text class="body-copy" x="564" y="173" font-size="16.5">lorem ipsum lorem ipsum</text>

    <line class="brand-rule" x1="871" y1="37" x2="871" y2="224"/>

    <text class="headline" x="930" y="106" font-size="33">BUSINESS <tspan class="accent">PAGE</tspan></text>
    <text class="body-copy" x="930" y="130" font-size="16.5">Lorem ipsum lorem ipsum, lorem</text>
    <text class="body-copy" x="930" y="151" font-size="16.5">ipsum lorem ipsum lorem ipsum</text>
    <text class="body-copy" x="930" y="173" font-size="16.5">lorem ipsum lorem ipsum</text>
  </svg>

  <p class="size-label size-label--business">1536 x 768</p>
  <svg class="banner banner--business" viewBox="0 0 998 499" aria-label="Careerloom business page banner">
    <polygon class="stripe-navy" points="394,0 490,0 633,281 538,283"/>
    <polygon class="stripe-amber" points="601,200 696,200 851,499 752,499"/>

    <circle class="brand-mark" cx="843" cy="62" r="36"/>
    <text class="brand-name" x="843" y="175" font-size="50" text-anchor="middle">Keelstone</text>
    <text class="brand-name" x="843" y="205" font-size="28" text-anchor="middle" letter-spacing="3">Advisory</text>

    <text class="headline" x="75" y="230" font-size="42">BUSINESS <tspan class="accent">PAGE</tspan></text>
    <text class="body-copy" x="75" y="262" font-size="21">Lorem ipsum lorem ipsum, lorem</text>
    <text class="body-copy" x="75" y="288" font-size="21">ipsum lorem ipsum lorem ipsum</text>
    <text class="body-copy" x="75" y="315" font-size="21">lorem ipsum lorem ipsum</text>
  </svg>
</main>
</body>
</html>
```